Need a business card for our overland brand!

We had the logo made and we need a great design for our business card. Use the logo provide or tweak it however you see fit.

Contact Information for Business Card

Name, Title, Telephone, email, website

```html
<!DOCTYPE html>
<html lang="en">
<head>
<meta charset="utf-8">
<title>Highpass Traverse – Business Card</title>
<link rel="stylesheet" href="https://fonts.googleapis.com/css2?family=Bebas+Neue&family=Montserrat:wght@500;600&display=swap">
<style>
  :root {
    --navy: #253850;
    --sky: #1d9fc4;
    --white: #ffffff;
    --backdrop: #e6e8ea;
  }
  * { margin: 0; padding: 0; box-sizing: border-box; }
  html, body {
    width: 858px;
    height: 1200px;
    overflow: hidden;
    background: var(--backdrop);
  }
  .sheet {
    position: relative;
    width: 858px;
    height: 1200px;
  }
  .card {
    position: absolute;
    left: 79px;
    width: 700px;
    height: 400px;
    overflow: hidden;
    box-shadow: 0 6px 18px rgba(0,0,0,0.18);
  }
  .card--front { top: 150px; background: var(--navy); }
  .card--back  { top: 650px; background: var(--navy); }

  .front-shapes {
    position: absolute;
    inset: 0;
  }
  .brand-mark {
    position: absolute;
    left: 236px;
    top: 150px;
    width: 280px;
    text-align: center;
    font-family: "Bebas Neue", sans-serif;
    font-weight: 400;
    font-size: 88px;
    line-height: 0.86;
    color: var(--white);
    letter-spacing: 0.5px;
  }

  .back-split {
    position: absolute;
    top: 0;
    right: 0;
    width: 350px;
    height: 100%;
    background: var(--sky);
  }
  .back-name {
    position: absolute;
    left: 0;
    width: 330px;
    top: 183px;
    text-align: center;
    font-family: "Bebas Neue", sans-serif;
    font-size: 34px;
    line-height: 1;
    color: var(--white);
  }
  .contact-pill {
    position: absolute;
    left: 330px;
    top: 155px;
    width: 40px;
    height: 90px;
    border-radius: 20px;
    background: var(--white);
  }
  .contact-pill svg { position: absolute; left: 0; top: 0; }
  .contact-lines {
    position: absolute;
    left: 400px;
    top: 174px;
    font-family: "Montserrat", sans-serif;
    font-weight: 600;
    font-size: 17px;
    line-height: 27px;
    color: var(--white);
  }
  .website {
    position: absolute;
    left: 0;
    width: 700px;
    top: 350px;
    text-align: center;
    font-family: "Montserrat", sans-serif;
    font-weight: 500;
    font-size: 14px;
    letter-spacing: 9px;
    color: var(--white);
  }
</style>
</head>
<body>
<main class="sheet">

  <section class="card card--front" aria-label="Business card front">
    <svg class="front-shapes" width="700" height="400" viewBox="0 0 700 400">
      <polygon points="0,0 201,0 4,400 0,400" fill="var(--white)"/>
      <polygon points="62,290 207,400 4,400" fill="var(--sky)"/>
    </svg>
    <div class="brand-mark">Highpass<br>Traverse</div>
  </section>

  <section class="card card--back" aria-label="Business card back">
    <div class="back-split"></div>
    <div class="back-name">Highpass Traverse</div>

    <div class="contact-pill">
      <svg width="40" height="90" viewBox="0 0 40 90">
        <rect x="15" y="20" width="10" height="16" rx="1.5" fill="none" stroke="var(--navy)" stroke-width="1.6"/>
        <line x1="18" y1="33" x2="22" y2="33" stroke="var(--navy)" stroke-width="1.4"/>
        <rect x="14" y="57" width="12" height="8" fill="var(--navy)"/>
        <polyline points="14,57 20,62 26,57" fill="none" stroke="var(--white)" stroke-width="1"/>
      </svg>
    </div>

    <div class="contact-lines">
      <div class="contact-phone">+1 555 014 2783</div>
      <div class="contact-email">info@highpasstraverse.com</div>
    </div>

    <div class="website">www.highpasstraverse.com</div>
  </section>

</main>
</body>
</html>
```